Flyer for family counseling

For my family counseling I'm looking for a design for flyers. Important is not only the appearance of the flyer, but also the content design. All important contents can be found on my website: www.brigitte-volkanter.at The following items should NOT appear on the flyer: - constellation work - bereavement and palliative work My logo should definitely be on the flyer. Source files are available.

Target Market(s)

Families, individuals, children, couples in need of psychological support.

Colors

Designer to choose colors to be used in the design.

Requirements
Must have
• My logo - source files available Website and contact data Recognition value from website to flyer and vice versa
Should not have
• Mention of the constellation work and mourning and palliative work not desired.

```html
<!DOCTYPE html>
<html lang="en">
<head>
<meta charset="utf-8">
<title>Family Counseling Flyer</title>
<link href="https://fonts.googleapis.com/css2?family=Lato:wght@400;700&display=swap" rel="stylesheet">
<style>
:root{
  --bg:#5a5a5a;
  --paper:#ffffff;
  --blue:#1a6fb5;
  --teal:#14a39a;
  --ink:#3a3a3a;
  --grey:#6b6b6b;
}
*{margin:0;padding:0;box-sizing:border-box}
html,body{width:762px;height:1200px;overflow:hidden;background:var(--bg)}
body{position:relative;font-family:'Lato',sans-serif;color:var(--ink)}
.page{position:absolute;top:354px;width:350px;height:492px;background:var(--paper);overflow:hidden;box-shadow:0 2px 8px rgba(0,0,0,.35)}
.front{left:22px}
.back{left:392px}
.front-art{position:absolute;inset:0}
.brand{position:absolute;top:214px;left:0;width:350px;text-align:center}
.brand-mark{display:block;margin:0 auto 14px;width:26px;height:26px;border-radius:50%;background:var(--blue)}
.brand-name{font-size:12px;font-weight:400;color:var(--blue);letter-spacing:.5px}
.brand-line{font-size:6.5px;letter-spacing:4.2px;color:var(--blue);margin-top:2px}
.banner{position:absolute;top:302px;left:68px;width:240px;height:21px;background:var(--teal);color:#fff;font-size:12.5px;font-weight:700;text-align:center;line-height:21px;clip-path:polygon(2% 0,100% 0,98% 100%,0 100%)}
.front-copy{position:absolute;top:340px;left:20px;width:310px;text-align:center;font-size:6px;line-height:1.45;color:var(--ink)}
.front-copy .kicker{color:var(--blue);font-weight:700;font-size:6.8px;margin:2px 0}
.front-copy p{margin-bottom:4px}
.topic-list{display:grid;grid-template-columns:113px 90px;padding-left:72px;text-align:left;margin-top:1px}
.topic-list ul{list-style:none}
.topic-list li::before{content:"\2022";color:var(--blue);margin-right:2px}
.site{position:absolute;font-size:6.5px;font-weight:700;color:var(--ink)}
.front .site{top:472px;left:0;width:350px;text-align:center}
.tile{position:absolute;width:90px;height:64px;border-radius:8px}
.caption{position:absolute;width:110px;text-align:center;font-size:6.6px;color:var(--teal)}
.caption small{display:block;font-size:5px;color:var(--grey);margin-top:1px}
.headline{position:absolute;left:20px;font-size:10px;color:var(--blue)}
.body{position:absolute;left:20px;width:312px;font-size:4.8px;line-height:1.45;color:var(--ink)}
.body p{margin-bottom:3px}
.fills{display:flex;justify-content:space-between;padding:0 10px 0 30px}
.quote{position:absolute;left:20px;top:331px;width:140px;text-align:center;font-size:4.8px;line-height:1.4}
.quote .mark{color:var(--teal);font-size:9px;line-height:.6;display:block}
.footer-wave{position:absolute;left:0;bottom:0}
.contact{position:absolute;left:200px;top:455px;font-size:6.5px;font-weight:400;line-height:1.35;color:#fff}
.back .site{left:12px;top:478px}
</style>
</head>
<body>

<section class="page front">
  <svg class="front-art" width="350" height="492" viewBox="0 0 350 492">
    <defs>
      <linearGradient id="heroTone" x1="0" y1="0" x2="1" y2="1">
        <stop offset="0" stop-color="#e9d2b0"/>
        <stop offset=".35" stop-color="#d9b36a"/>
        <stop offset=".6" stop-color="#c9d99a"/>
        <stop offset="1" stop-color="#e8dfd6"/>
      </linearGradient>
      <linearGradient id="roomTone" x1="0" y1="0" x2="1" y2="1">
        <stop offset="0" stop-color="#efe7d8"/>
        <stop offset="1" stop-color="#b89a74"/>
      </linearGradient>
    </defs>
    <rect width="350" height="330" fill="url(#heroTone)" role="img" aria-label="Photo of a smiling mother with two daughters doing crafts at a table"/>
    <path d="M-20 330 A195 195 0 0 1 360 300 L360 492 L-20 492 Z" fill="#fff"/>
    <path d="M-20 330 A195 195 0 0 1 360 300" fill="none" stroke="#14a39a" stroke-width="7" transform="translate(-6,-8)"/>
    <path d="M0 318 A195 195 0 0 1 290 214" fill="none" stroke="#1a6fb5" stroke-width="9"/>
    <circle cx="288" cy="202" r="32" fill="#fff"/>
    <circle cx="288" cy="202" r="29" fill="url(#roomTone)" role="img" aria-label="Photo of a family talking together in a bright counseling room"/>
  </svg>

  <div class="brand">
    <span class="brand-mark"></span>
    <div class="brand-name">BRIGITTE VOLKANTER</div>
    <div class="brand-line">FAMILIENBERATUNG WIEN</div>
  </div>

  <div class="banner">Family and couples counseling</div>

  <div class="front-copy">
    <p>Every family goes through times in which living together becomes difficult.<br>Counseling offers a protected space to look at the situation from the outside - this opens<br>up a clearer view and allows different, but also new perspectives.</p>
    <div class="kicker">Statements like</div>
    <p>"Bringing the golden flow of love back to life." Or<br>"Every problem already carries the seed of its solution within itself."<br>guide me in my intention.</p>
    <p style="margin-bottom:1px">Respect and appreciation in working with my clients are very important to me.<br>Counseling can support you on a variety of topics, such as:</p>
    <div class="topic-list">
      <ul><li>Family conflicts</li><li>Separation and divorce</li><li>Parenting questions</li><li>Stress and crises</li></ul>
      <ul><li>Decisions</li><li>Aims</li><li>Resources</li><li>And much more.</li></ul>
    </div>
  </div>

  <div class="site">www.brigitte-volkanter.at</div>
</section>

<section class="page back">
  <div class="tile" style="left:20px;top:18px;background:linear-gradient(135deg,#e8e2d2,#3a3a3a)" role="img" aria-label="Photo of an individual counseling room with armchairs"></div>
  <div class="tile" style="left:129px;top:18px;background:linear-gradient(135deg,#efe6d4,#5a4a3a)" role="img" aria-label="Photo of a couple in a counseling session"></div>
  <div class="tile" style="left:239px;top:18px;background:linear-gradient(135deg,#d9dde4,#8a3a40)" role="img" aria-label="Photo of children playing with a counselor"></div>
  <div class="tile" style="left:20px;top:118px;background:linear-gradient(135deg,#f0ece4,#b8863a)" role="img" aria-label="Photo of a family standing together in a room"></div>
  <div class="tile" style="left:129px;top:118px;background:linear-gradient(135deg,#f2ead8,#c89a58)" role="img" aria-label="Photo of parents talking with a counselor"></div>
  <div class="tile" style="left:239px;top:118px;background:linear-gradient(135deg,#9a9a9a,#2a2a2a)" role="img" aria-label="Black and white photo of supporting hands"></div>

  <div class="caption" style="left:10px;top:87px">individual counseling<small>Unauthorized from the crisis</small></div>
  <div class="caption" style="left:119px;top:87px">Couples counseling<small>Basis and new beginning</small></div>
  <div class="caption" style="left:229px;top:87px">child guidance<small>guide - lead - accompany</small></div>
  <div class="caption" style="left:10px;top:189px">Family &amp; children<small>Living together</small></div>
  <div class="caption" style="left:109px;top:189px;width:130px">parent counseling<small>Support in everyday parenting</small></div>
  <div class="caption" style="left:229px;top:189px">Life crises<small>Finding new footing</small></div>

  <div class="headline" style="top:218px">Has your life reached a point where change is needed?</div>
  <div class="body" style="top:233px">
    <p>Are ...</p>
    <p class="fills"><span>... trained ...</span><span>... inappropriate ...</span><span>... unpleasant ...</span><span>... deadlocked ...</span><span>... retracted ...</span></p>
    <p>... dissolve patterns of behavior? No longer useful?</p>
    <p>Going new ways and / or mastering challenging life situations are a gift and offer a chance to develop as a person if they are recognized as such.</p>
    <p>I accompany you through empathetic discussions, help you develop your potential and make your resources visible. Impulses are set to discover the great possibilities that life holds for you.</p>
    <p>Together we work out new perspectives and open up ways that give you strength and courage.</p>
  </div>

  <div class="headline" style="top:312px">Strength for every stage of life</div>
  <div class="quote">
    <span class="mark">&ldquo;</span>
    You are important because you are you.<br>Every person carries the strength to grow.<br>Together we find the steps that help you<br>to live calmly and confidently again.
    <span class="mark">&rdquo;</span>
  </div>
  <div class="tile" style="left:170px;top:309px;width:92px;height:64px;border-radius:0;background:radial-gradient(circle at 45% 55%,#8a6a5a,#dfe8e6 70%)" role="img" aria-label="Photo of balanced stacked stones"></div>

  <div class="body" style="top:380px">
    <p style="margin-bottom:1px">Families, couples, individuals and children are welcome to come to me - whether in acute crises or when you simply feel that something needs to change.</p>
    <p style="margin-bottom:1px">Counseling is confidential and takes place in a calm, friendly setting in Vienna. Appointments are arranged individually by phone or email.</p>
    <p style="margin-bottom:0">Accompanying families and individuals means for me offering ...<br>... closeness and presence<br>... encouragement to be honest about feelings<br>... support in finding new ways of talking with each other<br>... time and space for what really matters to you</p>
  </div>

  <svg class="footer-wave" width="350" height="60" viewBox="0 0 350 60">
    <path d="M110 60 C160 20 260 4 350 2 L350 60 Z" fill="#14a39a"/>
    <path d="M130 60 C180 26 270 12 350 10 L350 60 Z" fill="#1a6fb5"/>
  </svg>
  <div class="contact">Lindengasse 14/3, 1070 Vienna<br>familienberatung@brigitte-volkanter.at<br>Telephone: +43 676 118 42 90</div>
  <div class="site">www.brigitte-volkanter.at</div>
</section>

</body>
</html>
```